Rainbow card

Looking for someone to design a card using rainbow theme and link 7 different promises of love to each color. The design will be used to either print a greeting card for valentines or flyer type layout to be framed.

Target Market(s)

Personal

Font styles to use
Script

Colors
eb1f27
f78f20
faee3e
9bcb3c
0655a3
6a429a
a64599

Requirements
Must have
• Rainbow
• The phrases to be included on each color are:
• red - I'll never leave you as long as you'll have me.
• orange - I'll never deny you my body.
• yellow - I'll never let you go to prison.
• green - I'll have a baby with you.
• blue - I'll marry you.
• Indigo - I'll always love you.
• Violet - I'll always stand by you and support you.
Nice to have
• Rainbow, love and loyalty significance

```html
<!DOCTYPE html>
<html lang="en">
<head>
<meta charset="utf-8">
<title>Seven Promises – Rainbow Card</title>
<link rel="stylesheet" href="https://fonts.googleapis.com/css2?family=Petit+Formal+Script&display=swap">
<style>
  :root {
    --red: #eb1f27;
    --orange: #f78f20;
    --yellow: #faee3e;
    --green: #9bcb3c;
    --blue: #0655a3;
    --indigo: #6a429a;
    --violet: #a64599;
    --bg-left: #9bcb3c;
    --bg-mid: #3f2a78;
    --bg-right: #f08a35;
    --ground: #3aa04a;
    --outline: #ffffff;
    --ink-light: #ffffff;
    --ink-dark: #3a2a10;
  }
  html, body {
    margin: 0;
    padding: 0;
    overflow: hidden;
    background: #ffffff;
  }
  .card {
    position: relative;
    width: 1200px;
    height: 923px;
    overflow: hidden;
    background: linear-gradient(90deg,
      var(--bg-left) 0%,
      #5f8a6a 22%,
      #2f4f88 42%,
      var(--bg-mid) 52%,
      #6a3f86 62%,
      #b06a6a 80%,
      var(--bg-right) 100%);
    font-family: "Petit Formal Script", cursive;
  }
  .rainbow, .ground {
    position: absolute;
    left: 0;
    top: 0;
  }
  .vow {
    font-family: "Petit Formal Script", cursive;
    font-size: 17px;
    font-weight: 400;
  }
  .vow--light { fill: var(--ink-light); }
  .vow--dark { fill: var(--ink-dark); }
  .decor {
    position: absolute;
    border-radius: 50%;
  }
  .decor--leaves-left {
    left: 10px; top: -20px; width: 380px; height: 270px;
    background: radial-gradient(ellipse at center, rgba(184,215,122,.85) 0%, rgba(120,170,80,.45) 55%, rgba(120,170,80,0) 72%);
  }
  .decor--leaves-right {
    left: 1000px; top: -10px; width: 220px; height: 400px;
    background: radial-gradient(ellipse at center, rgba(184,215,122,.85) 0%, rgba(120,170,80,.45) 55%, rgba(120,170,80,0) 72%);
  }
  .decor--yellow-flowers {
    left: 30px; top: 570px; width: 230px; height: 340px;
    background: radial-gradient(ellipse at center, rgba(245,216,74,.8) 0%, rgba(60,150,60,.5) 55%, rgba(60,150,60,0) 72%);
  }
  .decor--white-flowers {
    left: 1030px; top: 560px; width: 170px; height: 360px;
    background: radial-gradient(ellipse at center, rgba(238,243,251,.85) 0%, rgba(60,150,60,.5) 55%, rgba(60,150,60,0) 72%);
  }
  .decor--herb {
    left: 850px; top: 770px; width: 180px; height: 160px;
    background: radial-gradient(ellipse at center, rgba(184,215,122,.85) 0%, rgba(80,140,60,.5) 55%, rgba(80,140,60,0) 72%);
  }
  .steps {
    position: absolute;
    left: 340px;
    top: 425px;
    margin: 0;
    padding: 0;
    list-style: none;
  }
  .steps__item {
    height: 65.5px;
    font-size: 27px;
    line-height: 65.5px;
    white-space: nowrap;
    -webkit-text-stroke: 0.5px var(--outline);
  }
  .steps__item--red { color: var(--red); }
  .steps__item--orange { color: var(--orange); }
  .steps__item--yellow { color: var(--yellow); }
  .steps__item--green { color: var(--green); }
  .steps__item--blue { color: var(--blue); }
  .steps__item--indigo { color: var(--indigo); }
  .steps__item--violet { color: var(--violet); }
  .headline {
    position: absolute;
    left: 622px;
    top: 672px;
    margin: 0;
    font-weight: 400;
    font-size: 44px;
    line-height: 1;
    color: var(--orange);
    -webkit-text-stroke: 0.7px var(--outline);
    white-space: nowrap;
  }
</style>
</head>
<body>
<main class="card">
  <svg class="rainbow" width="1200" height="923" viewBox="0 0 1200 923">
    <defs>
      <filter id="band-blur" x="-10%" y="-10%" width="120%" height="120%">
        <feGaussianBlur stdDeviation="7"/>
      </filter>
      <path id="arc-red" d="M39 333.8 A978 978 0 0 1 1161 333.8"/>
      <path id="arc-orange" d="M57.9 360.9 A945 945 0 0 1 1142.1 360.9"/>
      <path id="arc-yellow" d="M76.9 387.9 A912 912 0 0 1 1123.1 387.9"/>
      <path id="arc-green" d="M95.8 414.9 A879 879 0 0 1 1104.2 414.9"/>
      <path id="arc-blue" d="M114.7 441.9 A846 846 0 0 1 1085.3 441.9"/>
      <path id="arc-indigo" d="M133.7 469 A813 813 0 0 1 1066.3 469"/>
      <path id="arc-violet" d="M152.6 496 A780 780 0 0 1 1047.4 496"/>
    </defs>
    <g fill="none" stroke-width="36" filter="url(#band-blur)" aria-hidden="true">
      <circle cx="600" cy="1135" r="985" stroke="var(--red)"/>
      <circle cx="600" cy="1135" r="952" stroke="var(--orange)"/>
      <circle cx="600" cy="1135" r="919" stroke="var(--yellow)"/>
      <circle cx="600" cy="1135" r="886" stroke="var(--green)"/>
      <circle cx="600" cy="1135" r="853" stroke="var(--blue)"/>
      <circle cx="600" cy="1135" r="820" stroke="var(--indigo)"/>
      <circle cx="600" cy="1135" r="787" stroke="var(--violet)"/>
    </g>
    <g class="vows" text-anchor="middle">
      <text class="vow vow--light"><textPath href="#arc-red" startOffset="50%">I'll never leave you as long as you'll have me.</textPath></text>
      <text class="vow vow--dark"><textPath href="#arc-orange" startOffset="50%">I'll never deny you my body.</textPath></text>
      <text class="vow vow--dark"><textPath href="#arc-yellow" startOffset="50%">I'll never let you go to prison.</textPath></text>
      <text class="vow vow--dark"><textPath href="#arc-green" startOffset="50%">I'll have a baby with you.</textPath></text>
      <text class="vow vow--light"><textPath href="#arc-blue" startOffset="50%">I'll marry you.</textPath></text>
      <text class="vow vow--light"><textPath href="#arc-indigo" startOffset="50%">I'll always love you.</textPath></text>
      <text class="vow vow--light"><textPath href="#arc-violet" startOffset="50%">I'll always stand by you and support you.</textPath></text>
    </g>
  </svg>

  <div class="decor decor--leaves-left" role="img" aria-label="Illustrated sprigs of green leaves hanging from the top left corner"></div>
  <div class="decor decor--leaves-right" role="img" aria-label="Illustrated sprigs of green leaves hanging from the top right corner"></div>
  <div class="decor decor--yellow-flowers" role="img" aria-label="Illustrated stems of small yellow flowers with grass"></div>
  <div class="decor decor--herb" role="img" aria-label="Illustrated small leafy herb plant"></div>
  <div class="decor decor--white-flowers" role="img" aria-label="Illustrated stems of white bell flowers with grass"></div>

  <svg class="ground" width="1200" height="923" viewBox="0 0 1200 923" aria-hidden="true">
    <line x1="160" y1="915" x2="1195" y2="915" stroke="var(--ground)" stroke-width="2" stroke-dasharray="3 4"/>
  </svg>

  <ul class="steps">
    <li class="steps__item steps__item--red">One look</li>
    <li class="steps__item steps__item--orange">Two words</li>
    <li class="steps__item steps__item--yellow">Three steps</li>
    <li class="steps__item steps__item--green">Four sighs</li>
    <li class="steps__item steps__item--blue">Five emotions</li>
    <li class="steps__item steps__item--indigo">Six kisses</li>
    <li class="steps__item steps__item--violet">Seven dreams</li>
  </ul>

  <h1 class="headline">Seven promises</h1>
</main>
</body>
</html>
```